Simple proffessional BC

I have a logo which I will attach below.
I would like the logo on the front of the card with these details in point form below:
Pre and Post Natal Yoga: Pregnancy Workshops: Hypnobirthing Courses
On the back of the card my details:
Merrin Galvey
Facebook page- calmbellieswillowharbour
Mobile- 0438 512 740

I like the idea of the card being simple, possibly just the above on a plain coloured (eggshell?) card, a card that is textured.
I am open to suggestion if it appeals!
Thank you and good luck!

Target Market(s)

Pregnant women, 20's-40's

Requirements
Must have
• Simple, compliment logo.
Make logo the feature.
Should not have

• .

```html
<!DOCTYPE html>
<html lang="en">
<head>
<meta charset="utf-8">
<title>Calm Bellies – Business Card</title>
<link href="https://fonts.googleapis.com/css2?family=Questrial&display=swap" rel="stylesheet">
<style>
  :root {
    --backdrop: #e6e4e0;
    --card: #ffffff;
    --ink-red: #8b1d1f;
    --accent-orange: #eca33a;
    --card-shadow: rgba(0, 0, 0, 0.18);
  }
  * { box-sizing: border-box; margin: 0; padding: 0; }
  html, body {
    width: 1200px;
    height: 1000px;
    overflow: hidden;
    background: var(--backdrop);
    font-family: "Questrial", "Century Gothic", sans-serif;
  }
  .card-set {
    position: relative;
    width: 1200px;
    height: 1000px;
  }
  .card {
    position: absolute;
    top: 185px;
    width: 380px;
    height: 630px;
    background: var(--card);
    box-shadow: 0 6px 22px var(--card-shadow);
  }
  .card--contact { left: 170px; }
  .card--services { left: 650px; }

  /* Contact side */
  .brand {
    position: absolute;
    top: 42px;
    left: 34px;
    display: flex;
    align-items: center;
    gap: 16px;
  }
  .brand__dot {
    width: 62px;
    height: 62px;
    border-radius: 50%;
    background: var(--accent-orange);
  }
  .brand__name {
    font-size: 34px;
    color: var(--ink-red);
    letter-spacing: 0.5px;
  }
  .contact {
    position: absolute;
    top: 168px;
    left: 92px;
    color: var(--ink-red);
  }
  .contact__name {
    font-size: 34px;
    letter-spacing: 1px;
    line-height: 1.2;
  }
  .contact__phone {
    font-size: 29px;
    letter-spacing: 1px;
    color: #3b2320;
  }
  .contact__label { color: var(--accent-orange); }
  .feature-disc {
    position: absolute;
    left: 118px;
    top: 300px;
    width: 300px;
    height: 300px;
    border-radius: 50%;
    background: var(--accent-orange);
  }
  .card--contact { overflow: hidden; }

  /* Services side */
  .services {
    position: absolute;
    left: 44px;
    bottom: 118px;
    list-style: none;
    color: var(--ink-red);
    font-size: 23px;
    letter-spacing: 1px;
    line-height: 1.42;
  }
  .social {
    position: absolute;
    left: 44px;
    bottom: 72px;
    display: flex;
    align-items: center;
    gap: 10px;
    color: var(--ink-red);
    font-size: 15px;
    letter-spacing: 0.5px;
  }
  .social__mark {
    width: 14px;
    height: 14px;
    background: var(--accent-orange);
  }
</style>
</head>
<body>
  <main class="card-set">
    <section class="card card--contact">
      <div class="brand">
        <span class="brand__dot"></span>
        <span class="brand__name">Calm Bellies</span>
      </div>
      <div class="contact">
        <p class="contact__name">Merrin Galvey</p>
        <p class="contact__phone"><span class="contact__label">M:</span> 0438 512 740</p>
      </div>
      <div class="feature-disc"></div>
    </section>

    <section class="card card--services">
      <ul class="services">
        <li>Pre and Post Natal Yoga</li>
        <li>Pregnancy Workshops</li>
        <li>Hypnobirthing Courses</li>
      </ul>
      <p class="social">
        <span class="social__mark"></span>
        <span class="social__handle">calmbellieswillowharbour</span>
      </p>
    </section>
  </main>
</body>
</html>
```